Business cards for Wheelnest

We need a business card layout for our new bike and e-bike rental (we also sell used e-bikes and bike accessories). The logo already exists.

```html
<!DOCTYPE html>
<html lang="en">
<head>
<meta charset="utf-8">
<title>Wheelnest business cards</title>
<link href="https://fonts.googleapis.com/css2?family=Open+Sans:wght@400;600&family=Cabin:wght@500;600&display=swap" rel="stylesheet">
<style>
  :root {
    --canvas: #9a9a9a;
    --card-light: #ededed;
    --ink: #1d3138;
    --ink-soft: #2c3a40;
    --teal: #5fc3a6;
    --rule: #a9a9a9;
    --white: #ffffff;
  }
  * { margin: 0; padding: 0; box-sizing: border-box; }
  html, body { width: 1200px; height: 1200px; overflow: hidden; }
  body {
    background: var(--canvas);
    position: relative;
    font-family: "Open Sans", Arial, sans-serif;
    color: var(--ink);
  }
  .card {
    position: absolute;
    top: 310px;
    height: 594px;
    box-shadow: 2px 3px 4px rgba(0,0,0,0.35);
  }
  .card-front {
    left: 234px;
    width: 364px;
    background: var(--card-light);
    text-align: center;
  }
  .card-back {
    left: 627px;
    width: 370px;
    background: linear-gradient(to bottom, var(--ink) 0 59%, var(--teal) 59% 100%);
  }
  .brand-mark {
    position: absolute;
    left: 0; right: 0;
    top: 166px;
    display: flex;
    align-items: center;
    justify-content: center;
    gap: 12px;
  }
  .brand-dot {
    width: 16px; height: 16px;
    border-radius: 50%;
    background: var(--white);
  }
  .brand-name {
    font-weight: 400;
    font-size: 52px;
    letter-spacing: 0.5px;
    color: var(--teal);
    line-height: 1;
    white-space: nowrap;
  }
  .tagline {
    position: absolute;
    left: 0; right: 0;
    top: 256px;
    font-family: "Cabin", Arial, sans-serif;
    font-weight: 600;
    font-size: 21px;
    color: var(--ink);
  }
  .person {
    position: absolute;
    left: 78px; right: 78px;
    top: 334px;
    padding-bottom: 8px;
    border-bottom: 1px solid var(--rule);
  }
  .person-name { font-size: 21px; line-height: 26px; color: var(--ink); }
  .person-role { font-size: 16.5px; line-height: 20px; color: var(--ink-soft); }
  .contact {
    position: absolute;
    left: 78px; right: 78px;
    top: 399px;
    padding-bottom: 10px;
    border-bottom: 1px solid var(--rule);
    font-size: 16.5px;
    line-height: 21.5px;
    color: var(--ink-soft);
  }
  .contact b { font-weight: 600; color: var(--ink); }
  .contact .web { font-size: 17.5px; font-weight: 600; color: var(--ink); }
  .contact .web span { color: var(--teal); }
  .address {
    position: absolute;
    left: 0; right: 0;
    top: 505px;
    font-size: 16.5px;
    line-height: 21.5px;
    color: var(--ink-soft);
  }
  .back-mark {
    position: absolute;
    left: 0; right: 0;
    top: 246px;
    display: flex;
    align-items: center;
    justify-content: center;
    gap: 12px;
  }
  .back-mark .brand-name { font-size: 44px; color: var(--white); }
  .services {
    position: absolute;
    left: 0; right: 0;
    top: 505px;
    text-align: center;
    font-size: 14.5px;
    font-weight: 600;
    line-height: 19px;
    text-transform: uppercase;
    color: var(--ink);
  }
</style>
</head>
<body>
  <section class="card card-front">
    <div class="brand-mark">
      <span class="brand-name">WHEELNEST</span>
    </div>
    <p class="tagline">e-leicht unterwegs</p>
    <div class="person">
      <p class="person-name">LUKAS BRENNER</p>
      <p class="person-role">Managing Director</p>
    </div>
    <div class="contact">
      <p><b>P:</b> 044-318 702 215</p>
      <p><b>M:</b> 044-318 702 216</p>
      <p><b>E:</b> hello@wheelnest.ch</p>
      <p class="web">www.<span>wheelnest-rides</span>.ch</p>
    </div>
    <div class="address">
      <p>48 Kettenweg, Altstadt</p>
      <p>Switzerland, 8004.</p>
    </div>
  </section>

  <section class="card card-back">
    <div class="back-mark">
      <span class="brand-dot"></span>
      <span class="brand-name">WHEELNEST</span>
    </div>
    <div class="services">
      <p>New bike and e-bike rental</p>
      <p>Sell used e-bikes and bike accessories</p>
    </div>
  </section>
</body>
</html>
```